Sena & Kaan Wedding Invitation and Decorative Designs

We are looking for a sweet and elegant design for our wedding invitation. We need different versions of the same design to use both as printed hard copies and in digital formats (WhatsApp image, instagram post, etc) Please see attached sample invitation, which we like as a simple and elegant option, but also find it quite basic. We are open to creative suggestions following a similar style.
Once we decide on an invitation design, we would like to use the same design elements in guest name cards, welcome sign, menu cards and print cover for the dance floor of our wedding venue. Please see random samples of these materials attached. We also attach a photo from our wedding venue displaying a close to final visual of the decoration we chose for our wedding day (sharing in case it helps as an inspiration source and helps with matching decoration colors with the designs)
- Must have a style similar to the attached sample invitation

```html
<!DOCTYPE html>
<html lang="tr">
<head>
<meta charset="utf-8">
<title>Sena &amp; Kaan – Davetiye</title>
<link href="https://fonts.googleapis.com/css2?family=Macondo&family=Cormorant+Garamond:ital,wght@1,400&family=Sacramento&family=Open+Sans:wght@500&family=Fira+Sans+Condensed:ital@1&family=Della+Respira&display=swap" rel="stylesheet">
<style>
  :root {
    --paper: #ececec;
    --sage: #7fa784;
    --sage-line: #8fbf94;
    --sage-soft: #d3e3d4;
    --sage-soft-edge: #c2d9c4;
    --forest: #4f6650;
    --band-text: #ececec;
  }
  html, body {
    margin: 0;
    padding: 0;
    overflow: hidden;
    background: var(--paper);
  }
  .invitation {
    position: relative;
    width: 1200px;
    height: 1197px;
    background: var(--paper);
    overflow: hidden;
  }
  .message-band {
    position: absolute;
    left: 0;
    top: 604px;
    width: 1200px;
    height: 151px;
    background: var(--sage);
  }
  .frame-lines {
    position: absolute;
    inset: 0;
    width: 1200px;
    height: 1197px;
  }
  .frame-lines .rule {
    fill: none;
    stroke: var(--sage-line);
    stroke-width: 2.2;
    stroke-linecap: round;
  }
  .ornament {
    position: absolute;
    border-radius: 50%;
    background: radial-gradient(circle at 50% 50%, var(--sage-soft) 0%, var(--sage-soft-edge) 100%);
  }
  .ornament-top-left     { left: 546px; top: 58px;   width: 84px; height: 74px; }
  .ornament-top-right    { left: 750px; top: 205px;  width: 70px; height: 96px; }
  .ornament-middle-right { left: 568px; top: 465px;  width: 94px; height: 70px; }
  .ornament-left-top     { left: 357px; top: 186px;  width: 70px; height: 94px; }
  .ornament-left-bottom  { left: 283px; top: 830px;  width: 70px; height: 94px; }
  .ornament-bottom-right { left: 855px; top: 1050px; width: 70px; height: 94px; }
  .text {
    position: absolute;
    margin: 0;
    white-space: nowrap;
    transform: translateX(-50%);
    text-align: center;
    font-weight: 400;
  }
  .couple-name {
    font-family: "Macondo", serif;
    color: var(--forest);
    font-size: 60px;
    line-height: 1;
  }
  .bride { left: 560px; top: 188px; }
  .ampersand { left: 594px; top: 272px; font-size: 44px; }
  .groom { left: 658px; top: 322px; }
  .welcome-message {
    left: 619px;
    top: 624px;
    font-family: "Cormorant Garamond", serif;
    font-style: italic;
    font-size: 33px;
    line-height: 35px;
    color: var(--band-text);
    letter-spacing: 1px;
  }
  .invited {
    left: 598px;
    top: 768px;
    font-family: "Sacramento", cursive;
    font-size: 92px;
    line-height: 1;
    color: var(--sage);
  }
  .venue-name {
    left: 606px;
    top: 876px;
    font-family: "Open Sans", sans-serif;
    font-weight: 500;
    font-size: 43px;
    line-height: 1;
    color: var(--sage);
  }
  .venue-address {
    left: 611px;
    top: 942px;
    font-family: "Fira Sans Condensed", sans-serif;
    font-style: italic;
    font-size: 32px;
    line-height: 1;
    color: var(--sage);
  }
  .event-date {
    left: 614px;
    top: 1020px;
    font-family: "Della Respira", serif;
    font-size: 44px;
    line-height: 1;
    color: var(--sage);
  }
</style>
</head>
<body>
<main class="invitation">
  <div class="message-band"></div>

  <svg class="frame-lines" viewBox="0 0 1200 1197" aria-hidden="true">
    <line class="rule" x1="1197" y1="0" x2="1197" y2="761"/>

    <path class="rule" d="M0,42 H572 Q598,46 598,70"/>
    <path class="rule" d="M0,67 H575"/>

    <path class="rule" d="M809,0 V240"/>
    <path class="rule" d="M833,0 V235 Q830,258 810,262"/>

    <path class="rule" d="M652,524 H1197"/>
    <path class="rule" d="M612,520 Q612,546 634,548 H1197"/>

    <path class="rule" d="M342,860 V250 Q346,224 372,222"/>
    <path class="rule" d="M366,246 V860 Q362,884 340,886"/>

    <path class="rule" d="M913,755 V1085"/>
    <path class="rule" d="M937,755 V1082 Q933,1106 912,1108"/>
  </svg>

  <div class="ornament ornament-top-left" role="img" aria-label="Kıvrımlı köşe süsü"></div>
  <div class="ornament ornament-top-right" role="img" aria-label="Kıvrımlı köşe süsü"></div>
  <div class="ornament ornament-middle-right" role="img" aria-label="Kıvrımlı köşe süsü"></div>
  <div class="ornament ornament-left-top" role="img" aria-label="Kıvrımlı köşe süsü"></div>
  <div class="ornament ornament-left-bottom" role="img" aria-label="Kıvrımlı köşe süsü"></div>
  <div class="ornament ornament-bottom-right" role="img" aria-label="Kıvrımlı köşe süsü"></div>

  <h1 class="text couple-name bride">Sena</h1>
  <p class="text couple-name ampersand">&amp;</p>
  <h1 class="text couple-name groom">Kaan</h1>

  <p class="text welcome-message">Bu mutlu günümüzde sizleri de<br>aramızda görmekten mutluluk<br>duyacağız</p>

  <h2 class="text invited">Davetlisiniz</h2>
  <p class="text venue-name">Lavora</p>
  <p class="text venue-address">Kandilli, Yali Cad. No: 27, Uskudar, Istanbul</p>
  <p class="text event-date">24 Ağustos 2024</p>
</main>
</body>
</html>
```